Lydfern Primary School

We need to improve on our designs for a local School, Lydfern Primary.
One file contains the correct information required on the sign.
Our Mock ups are suggestions.
The School Uniform is blue -
We had these comments from our Client.
I can't decide whether to change the blue and try green to represent our commitment to outdoors, or maybe a combination of colours from the school badge, For the main sign options , I like them both but wondered if there was a way of combining the two? Slightly bigger badge.

I've included the files for the smaller signs if you were happy to provide a service to include all. We are a sign business focusing on other projects and external support will help. Thanks - Dermot.

```html
<!DOCTYPE html>
<html lang="en">
<head>
<meta charset="utf-8">
<title>Lydfern Primary School – Entrance Sign</title>
<link rel="stylesheet" href="https://fonts.googleapis.com/css2?family=Outfit:wght@500;600;700&display=swap">
<style>
  :root {
    --backdrop: #b3b3b3;
    --sign-blue: #2470b8;
    --outdoor-green: #7aab1e;
    --sign-white: #ffffff;
    --sun-orange: #f39714;
    --title-yellow: #ffe033;
    --welsh-green: #a3c828;
  }
  html, body {
    margin: 0;
    padding: 0;
    width: 1200px;
    height: 874px;
    overflow: hidden;
    background: var(--backdrop);
  }
  .sign {
    display: block;
    width: 1200px;
    height: 874px;
    font-family: "Outfit", sans-serif;
  }
  .sign__outer { fill: var(--outdoor-green); }
  .sign__body { fill: var(--sign-blue); }
  .sign__border { fill: var(--sign-white); }
  .badge__ring { fill: var(--sign-white); }
  .badge__disc { fill: var(--sun-orange); }
  .badge__name { fill: var(--sign-white); font-weight: 700; font-size: 27px; }
  .motto { fill: var(--sun-orange); font-weight: 600; font-size: 33px; }
  .title-en { fill: var(--title-yellow); font-weight: 700; font-size: 68px; }
  .title-rule { fill: var(--sun-orange); }
  .title-cy { fill: var(--welsh-green); font-weight: 700; font-size: 68px; }
  .contact { fill: var(--sign-white); font-weight: 600; font-size: 27px; }
  .phone-icon__disc { fill: var(--sign-white); }
  .phone-icon__handset { fill: var(--sign-blue); }
  .council-name { fill: var(--sign-white); font-weight: 600; font-size: 14px; }
</style>
</head>
<body>
<svg class="sign" viewBox="0 0 1200 874" xmlns="http://www.w3.org/2000/svg" aria-label="Lydfern Primary School entrance sign">
  <!-- Sign plate: outdoor green edge, white keyline, uniform blue face -->
  <g class="sign__plate">
    <rect class="sign__outer" x="222" y="282" width="756" height="406" rx="48"/>
    <circle class="sign__outer" cx="600" cy="296" r="150"/>
    <rect class="sign__border" x="234" y="294" width="732" height="382" rx="38"/>
    <circle class="sign__border" cx="600" cy="296" r="138"/>
    <rect class="sign__body" x="240" y="300" width="720" height="370" rx="33"/>
    <circle class="sign__body" cx="600" cy="296" r="132"/>
  </g>

  <!-- School badge (enlarged) -->
  <g class="badge" role="img" aria-label="Lydfern Primary school badge">
    <circle class="badge__ring" cx="600" cy="296" r="114"/>
    <circle class="badge__disc" cx="600" cy="296" r="109"/>
    <text class="badge__name" x="600" y="291" text-anchor="middle">Lydfern</text>
    <text class="badge__name" x="600" y="322" text-anchor="middle">Primary</text>
  </g>

  <!-- Mottos -->
  <text class="motto" x="268" y="362">Wings to fly</text>
  <text class="motto" x="946" y="362" text-anchor="end">Roots to Grow</text>

  <!-- School name -->
  <text class="title-en" x="270" y="470" textLength="660" lengthAdjust="spacingAndGlyphs">Lydfern Primary School</text>
  <rect class="title-rule" x="269" y="489" width="662" height="5" rx="2.5"/>
  <text class="title-cy" x="270" y="558" textLength="660" lengthAdjust="spacingAndGlyphs">Ysgol Gynradd Lydfern</text>

  <!-- Contact -->
  <text class="contact" x="828" y="611" text-anchor="end">Headteacher/Pennaeth - Mr J. Harlow</text>
  <g class="phone-icon">
    <circle class="phone-icon__disc" cx="515" cy="634" r="14"/>
    <path class="phone-icon__handset" d="M509 626c1-1 2.5-1 3 0l2 3c.5 1 0 2-1 2.5-.5.3-.5 1 0 2l2 2c1 .8 1.6.6 2 0 .6-1 1.6-1.4 2.5-.8l3 2c1 .6 1 2 0 3-2 2-5 2-9-1.5-4-3.5-6.5-7.5-4.5-12.2z"/>
  </g>
  <text class="contact" x="540" y="644">01632 960418</text>

  <!-- Council -->
  <text class="council-name" x="890" y="614" text-anchor="middle">Westmere</text>
  <text class="council-name" x="890" y="632" text-anchor="middle">Council</text>
</svg>
</body>
</html>
```